Wirenexa

I'm looking to much improve our current website wirenexa.com
Updates

Low design quality

Target Market(s)

Commercial clients (Not-Residentials)

Industry/Entity Type

Office buildings and Industrial clients

Coding

Coded - Design and coding required

Number of Pages Required

5+ page

Requirements
Must have
• Very professional structured low voltage cabling projects for Wi-Fi, Audio/Video conference rooms, Access Control systems, CCTV.

```html
<!DOCTYPE html>
<html lang="en">
<head>
<meta charset="utf-8">
<title>Wirenexa – Structured Cabling & Integrated Technology Systems</title>
<link href="https://fonts.googleapis.com/css2?family=Lexend:wght@400;500;600&family=Inter:wght@400;500;600;700&display=swap" rel="stylesheet">
<style>
:root{
  --red:#d42b1f;
  --red-dark:#a81d14;
  --ink:#1f1f1f;
  --text:#555;
  --muted:#8a8a8a;
  --line:#d9d9d9;
  --field:#e6e6e6;
  --soft:#f3f3f3;
  --charcoal:#3a3a3a;
  --white:#fff;
}
*{box-sizing:border-box;margin:0;padding:0}
html,body{width:1200px;height:5208px;overflow:hidden}
body{font-family:"Inter",sans-serif;color:var(--ink);background:var(--white)}
section,header,footer{position:relative;width:1200px}
.abs{position:absolute}
h1,h2,h3,.display{font-family:"Lexend",sans-serif;font-weight:500;color:var(--ink)}
.eyebrow{font-size:8px;font-weight:700;color:var(--red);text-transform:uppercase;letter-spacing:.3px;display:flex;align-items:center;gap:5px}
.eyebrow::before{content:"";width:7px;height:7px;background:var(--red);border-radius:50% 50% 50% 0;transform:rotate(-45deg)}
.btn{position:absolute;display:flex;align-items:center;justify-content:center;font-size:11px;font-weight:600;border-radius:1px;text-decoration:none}
.btn-red{background:var(--red);color:var(--white)}
.btn-outline{border:1.5px solid var(--red);color:var(--red);background:var(--white)}
.btn-white{background:var(--white);color:var(--red)}
.placeholder{position:absolute}

/* top */
.top{height:941px;background:linear-gradient(180deg,#fbfbfb,#f1f1f1)}
.site-header{position:absolute;left:0;top:0;width:1200px;height:93px;background:var(--white);border-bottom:5px solid var(--red);z-index:3}
.brand{position:absolute;display:flex;align-items:center;gap:6px;font-family:"Lexend",sans-serif;font-weight:600;color:var(--ink);line-height:1}
.brand-mark{background:var(--red)}
.nav{position:absolute;top:36px;left:355px;display:flex;gap:50px;font-size:16px;font-weight:500}
.nav a{color:var(--ink);text-decoration:none}
.nav a.active{color:var(--red)}
.phone{position:absolute;left:840px;top:32px;display:flex;align-items:center;gap:10px;color:var(--red);font-size:18px;font-weight:500}
.phone-ring{width:30px;height:30px;border-radius:50%;border:1.5px solid var(--red);display:flex;align-items:center;justify-content:center}
.hero-photo{left:535px;top:93px;width:665px;height:622px;background:linear-gradient(100deg,#ececec 0%,#d9cfcc 28%,#8c2a23 55%,#6b1510 100%)}
.stat-card{position:absolute;background:var(--white);border-radius:8px;box-shadow:0 6px 18px rgba(0,0,0,.18);padding:10px 12px;font-size:8px;color:var(--ink);z-index:2}
.stat-card b{font-size:9px;font-weight:700}
.hero-title{left:61px;top:248px;width:470px;font-size:38px;line-height:48px}
.hero-copy{left:61px;top:444px;width:440px;font-size:11.5px;line-height:15px;color:var(--text)}
.callback{left:61px;top:636px;width:1079px;height:305px;background:var(--white);box-shadow:0 8px 30px rgba(0,0,0,.12)}
.callback-panel{position:absolute;left:0;top:0;width:462px;height:305px;background:var(--red);clip-path:polygon(0 0,100% 0,93% 100%,0 100%);color:var(--white);padding:78px 38px}
.callback-panel h2{color:var(--white);font-size:34px;font-weight:600}
.field{position:absolute;background:var(--field);border-radius:3px;color:var(--muted);font-size:12px;padding:13px 22px}

/* features */
.features{height:759px}
.feat-img{background:linear-gradient(160deg,#6d6a60,#2b2a28)}
.exp-badge{left:180px;top:394px;width:177px;height:95px;background:var(--red);color:var(--white);border:3px solid var(--white);display:flex;flex-direction:column;align-items:center;justify-content:center;font-size:17px;line-height:22px;font-family:"Lexend",sans-serif}
.exp-badge b{font-weight:600;font-size:21px}
.check-list{left:97px;top:544px;list-style:none;font-size:13px;color:var(--red);font-weight:500;line-height:30px}
.check-list li::before{content:"» ";color:var(--muted)}
.feat-body{left:608px;top:95px;width:530px}
.feat-body h2{font-size:28px;line-height:38px;margin-top:10px}
.feat-body p{font-size:11px;line-height:14px;color:var(--text);margin-bottom:12px}
.feat-body h4{font-size:11.5px;color:var(--red);font-weight:700;margin-bottom:6px}

/* solutions */
.solutions{height:550px}
.center-head{position:absolute;left:0;width:1200px;text-align:center}
.center-head .eyebrow{justify-content:center}
.center-head h2{font-size:29px;line-height:38px;margin:8px 0 14px}
.center-head p{font-size:12px;line-height:16px;color:var(--muted)}
.sol-card{position:absolute;width:256px;height:118px;background:var(--white);box-shadow:0 4px 14px rgba(0,0,0,.13);display:flex;align-items:center;gap:14px;padding:0 18px}
.sol-card svg{flex:none}
.sol-card h3{font-family:"Inter",sans-serif;font-size:15px;font-weight:600;line-height:19px}
.sol-card p{font-size:10.5px;color:var(--muted);line-height:13px;margin-top:5px}

/* services */
.services{height:850px}
.svc-card{position:absolute;top:228px;width:347px;height:433px;background:var(--red);text-align:center;color:var(--white)}
.svc-photo{width:347px;height:289px;background:linear-gradient(170deg,#c9b34a,#3d6b4a 45%,#2e2e2e 75%,#d9d9d9)}
.svc-arrow{position:absolute;right:26px;top:26px;width:46px;height:46px;border:2px solid var(--white);border-radius:50%;display:flex;align-items:center;justify-content:center}
.svc-card h3{color:var(--white);font-size:19px;font-weight:600;margin-top:20px}
.svc-card p{font-size:10.5px;line-height:13px;margin:8px auto 0;width:250px}
.svc-card .btn{left:135px;top:385px;width:80px;height:33px;font-size:10.5px}
.svc-icons{position:absolute;top:699px;left:0;width:1200px}
.svc-icon{position:absolute;width:140px;margin-left:-70px;text-align:center;font-size:10px;font-weight:600;line-height:13px}
.svc-icon svg{display:block;margin:0 auto 8px}

/* why */
.why{height:486px;background:var(--soft)}
.why-photo{left:683px;top:0;width:517px;height:486px;background:linear-gradient(120deg,#b11d18 0%,#3a2a22 45%,#5d6b3a 80%,#2a2a24 100%)}
.why h2{position:absolute;left:61px;top:115px;font-size:29px;line-height:38px}
.why-copy{left:61px;top:205px;width:440px;font-size:11px;line-height:14px;color:var(--text)}
.why-item{position:absolute;top:272px;width:180px}
.why-item .dot{width:46px;height:46px;border-radius:50%;background:var(--red);display:flex;align-items:center;justify-content:center}
.why-item h4{font-size:12px;font-weight:600;margin:14px 0 8px}
.why-item p{font-size:10.5px;line-height:13px;color:var(--muted)}

/* partners */
.partners{height:343px}
.partner{position:absolute;top:168px;font-family:"Lexend",sans-serif;font-weight:600;font-size:28px;color:#2a4d7a;transform:translateX(-50%);white-space:nowrap}

/* quote */
.quote{height:641px;background:var(--charcoal);z-index:2}
.quote-photo{left:0;top:0;width:499px;height:641px;background:linear-gradient(150deg,#1d3a5c,#0f1e33 60%,#28486a)}
.quote h2{position:absolute;left:533px;top:40px;color:var(--white);font-size:34px;font-weight:600}
.quote-field{position:absolute;left:533px;width:622px;background:var(--white);border-radius:3px;color:#bbb;font-size:12px;padding:15px 18px}
.info-bar{position:absolute;left:22px;width:477px;height:56px;background:var(--red);border-radius:4px;color:var(--white);display:flex;align-items:center;gap:14px;padding:0 34px;font-size:11px;font-weight:600;box-shadow:0 4px 12px rgba(0,0,0,.25);white-space:nowrap}
.info-bar b{font-weight:700;font-size:12px}
.spacer{height:153px}

/* footer */
.footer{height:485px;background:var(--soft)}
.footer h4{position:absolute;font-size:16px;font-weight:600;font-family:"Inter",sans-serif}
.foot-links{position:absolute;list-style:none;font-size:12px;line-height:35px}
.foot-contact{position:absolute;font-size:11px;line-height:14px;color:var(--ink)}
.foot-contact b{font-size:10.5px}
.social{position:absolute;top:115px;left:328px;display:flex;gap:21px}
.social span{width:16px;height:16px;background:var(--ink);border-radius:3px}
.legal{position:absolute;left:61px;top:405px;width:1078px;border-top:1px solid var(--line);padding-top:24px;display:flex;justify-content:space-between;font-size:12px}
.legal nav{display:flex;gap:30px}
.legal nav a{color:var(--ink)}
</style>
</head>
<body>

<section class="top">
  <header class="site-header">
    <div class="brand" style="left:61px;top:28px;font-size:36px"><span class="brand-mark" style="width:36px;height:36px"></span>Wirenexa</div>
    <nav class="nav"><a class="active" href="#">Home</a><a href="#">About Us</a><a href="#">Services</a><a href="#">Contact</a></nav>
    <div class="phone"><span class="phone-ring"><svg width="14" height="14" viewBox="0 0 24 24" fill="none" stroke="#d42b1f" stroke-width="2"><path d="M5 3h4l2 5-3 2a12 12 0 0 0 6 6l2-3 5 2v4a2 2 0 0 1-2 2A17 17 0 0 1 3 5a2 2 0 0 1 2-2z"/></svg></span>(888)-555-0142</div>
    <a class="btn btn-red" style="left:1040px;top:30px;width:100px;height:36px">Contact Us</a>
  </header>

  <div class="placeholder hero-photo" role="img" aria-label="Technician in a white hard hat holding an open network panel in front of a red server rack"></div>
  <div class="stat-card" style="left:1048px;top:160px;width:124px;height:78px">Network Performance<br><b style="font-size:12px">98%</b><br>Uptime
    <svg class="abs" style="left:60px;top:48px" width="52" height="20"><polyline points="0,18 12,12 20,15 32,6 40,9 52,2" fill="none" stroke="#d42b1f" stroke-width="1.5"/></svg></div>
  <div class="stat-card" style="left:780px;top:268px;width:145px;height:66px;padding-left:36px"><svg class="abs" style="left:12px;top:18px" width="16" height="28"><rect x="2" y="2" width="12" height="24" rx="2" fill="none" stroke="#1f1f1f" stroke-width="1.5"/></svg><b>Fiber Backbone</b><br>Single-Mode<br>10Gbps<div style="width:60px;height:3px;background:#d42b1f;margin-top:4px"></div></div>
  <div class="stat-card" style="left:995px;top:515px;width:163px;height:85px;padding-left:50px;line-height:16px"><span class="abs" style="left:12px;top:22px;width:28px;height:28px;border-radius:50%;border:1.5px solid #1f1f1f"></span><b>Security System</b><br>24/7 Monitoring<br><span style="color:#d42b1f">●</span> Active</div>

  <div class="abs eyebrow" style="left:61px;top:226px">Commercial low voltage solutions</div>
  <h1 class="abs hero-title">Structured Cabling &amp; Integrated Technology Systems for Commercial Environments</h1>
  <p class="abs hero-copy">Wirenexa delivers professional structured cabling, fiber optics, surveillance systems, access control, wireless networking, conference room technology, and commercial infrastructure solutions for offices, warehouses, retail spaces, and industrial facilities.</p>
  <a class="btn btn-red" style="left:61px;top:535px;width:159px;height:35px">Request Consultation</a>
  <a class="btn btn-outline" style="left:239px;top:535px;width:161px;height:35px">Explore Services</a>

  <div class="abs callback">
    <div class="callback-panel">
      <h2>Request Callback</h2>
      <div class="display" style="font-size:23px;margin:6px 0 18px;color:#fff">(888)-555-0142</div>
      <p style="font-size:12px">Submit the form and we will contact you within 1 hour.</p>
    </div>
    <div class="field" style="left:474px;top:36px;width:580px;height:46px">Name Here</div>
    <div class="field" style="left:474px;top:102px;width:277px;height:45px">Phone No</div>
    <div class="field" style="left:769px;top:102px;width:285px;height:45px">Email Id</div>
    <div class="field" style="left:474px;top:167px;width:580px;height:67px">Message</div>
    <a class="btn btn-red" style="left:894px;top:254px;width:160px;height:38px">Request Consultation</a>
  </div>
</section>

<section class="features">
  <div class="placeholder feat-img" style="left:97px;top:149px;width:221px;height:380px" role="img" aria-label="Electrician working inside an open distribution panel"></div>
  <div class="placeholder feat-img" style="left:333px;top:212px;width:229px;height:392px;background:linear-gradient(160deg,#7a7d80,#c9b833 60%,#3a3a3a)" role="img" aria-label="Technician in a hard hat and safety vest wiring a network cabinet"></div>
  <div class="abs exp-badge"><span><b>30+</b> Years</span><span>Experience</span></div>
  <ul class="abs check-list"><li>Copper CAT6 and CAT7</li><li>Single and Multimode Fiber</li><li>Wi-Fi Installation</li></ul>

  <div class="abs feat-body">
    <div class="eyebrow">Features</div>
    <h2>Built for Performance,<br>Security &amp; Scalability</h2>
    <p style="margin:8px 0 22px">Enterprise-grade low voltage systems engineered for modern commercial environments, ensuring reliable connectivity, security, and long-term operational efficiency.</p>
    <h4>Expertise and Experience:</h4>
    <p>With years of experience in the industry, our team brings a wealth of expertise to every cabling project. Whether you're a small office or a large industrial warehouse, we have the knowledge and skills to handle jobs of any size and complexity.</p>
    <h4>Comprehensive Solutions:</h4>
    <p>From copper CAT6 and CAT7 cabling to fiber optic installations (single and multimode) and Wi-Fi setup, we offer a full range of low voltage cabling services to meet your specific needs. Our solutions are tailored to your requirements, ensuring seamless connectivity and optimal performance.</p>
    <h4>Quality Workmanship:</h4>
    <p>At Wirenexa, we take pride in our work and strive for excellence in every project we undertake. Our cabling work is engineered and implemented with care and attention to detail, ensuring reliability, durability, and long-term performance.</p>
    <h4>Commercial and Industrial:</h4>
    <p>Whether you're a commercial business or an industrial facility, we have the expertise and resources to support your cabling needs. From office buildings to industrial plants, we have the capabilities to handle diverse environments and requirements.</p>
    <h4>Customer Satisfaction:</h4>
    <p>Our commitment to customer satisfaction drives everything we do. We work closely with our clients to understand their needs and deliver tailored solutions that exceed their expectations. Your satisfaction is our top priority.</p>
  </div>
  <a class="btn btn-red" style="left:608px;top:679px;width:98px;height:35px">Know More</a>
</section>

<section class="solutions">
  <div class="center-head" style="top:46px">
    <div class="eyebrow">Solutions</div>
    <h2>Complete Low Voltage Infrastructure<br>Solutions</h2>
    <p>Scalable commercial technology systems designed for<br>performance, security, and reliability.</p>
  </div>
  <div class="sol-card" style="left:61px;top:245px"><svg width="46" height="52" fill="none" stroke="#555" stroke-width="1.6"><path d="M12 4v14M20 4v14M8 18h16v8H8zM16 26v12c0 6 10 6 10 0V20M26 20h8v-8"/></svg><div><h3>Structured Cabling</h3><p>CAT6, CAT6A, fiber backbone systems.</p></div></div>
  <div class="sol-card" style="left:336px;top:245px"><svg width="46" height="52" fill="none" stroke="#555" stroke-width="1.6"><path d="M10 4v18l8 10v16M22 4v28M34 4v18l-8 10v16"/></svg><div><h3>Fiber Optic Solutions</h3><p>High-speed single-mode &amp; multimode fiber</p></div></div>
  <div class="sol-card" style="left:611px;top:245px"><svg width="52" height="52" fill="none" stroke="#555" stroke-width="1.6"><path d="M6 14l30 10-4 8-30-10zM20 28l-4 10H4M40 22l8-4v12l-8-4"/></svg><div><h3>CCTV &amp; Surveillance</h3><p>Enterprise video security systems.</p></div></div>
  <div class="sol-card" style="left:886px;top:245px"><svg width="46" height="52" fill="none" stroke="#555" stroke-width="1.6"><rect x="8" y="4" width="30" height="44" rx="3"/><rect x="14" y="12" width="18" height="10"/><path d="M14 30h4M22 30h4M30 30h2M14 38h4M22 38h4M30 38h2"/></svg><div><h3>Access Control</h3><p>Secure commercial entry management</p></div></div>
  <div class="sol-card" style="left:61px;top:385px"><svg width="46" height="52" fill="none" stroke="#555" stroke-width="1.6"><path d="M4 20a28 28 0 0 1 38 0M10 27a18 18 0 0 1 26 0M16 34a9 9 0 0 1 14 0"/><circle cx="23" cy="40" r="2"/></svg><div><h3>Wireless Networking</h3><p>Commercial Wi-Fi &amp; WAP deployment</p></div></div>
  <div class="sol-card" style="left:336px;top:385px"><svg width="50" height="52" fill="none" stroke="#555" stroke-width="1.6"><rect x="10" y="4" width="30" height="20"/><circle cx="12" cy="34" r="4"/><circle cx="25" cy="34" r="4"/><circle cx="38" cy="34" r="4"/><path d="M4 48c0-6 16-6 16 0M17 48c0-6 16-6 16 0M30 48c0-6 16-6 16 0"/></svg><div><h3>Conference Room Technology</h3><p>Audio/video collaboration systems.</p></div></div>
  <div class="sol-card" style="left:611px;top:385px"><svg width="46" height="52" fill="none" stroke="#555" stroke-width="1.6"><rect x="12" y="4" width="24" height="44" rx="3"/><rect x="17" y="10" width="14" height="10"/><path d="M17 28h4M27 28h4M17 36h4M27 36h4M4 24h8v14H4z"/></svg><div><h3>Point of Sale Infrastructure</h3><p>Retail POS connectivity solutions.</p></div></div>
  <div class="sol-card" style="left:886px;top:385px"><svg width="46" height="52" fill="none" stroke="#555" stroke-width="1.6"><path d="M8 14a20 20 0 0 0 26 26zM21 27l10-10M30 10a10 10 0 0 1 8 8M30 4a16 16 0 0 1 14 14M16 36l-6 12h16"/></svg><div><h3>Satellite &amp; Connectivity</h3><p>Reliable remote internet deployment.</p></div></div>
</section>

<section class="services">
  <div class="center-head" style="top:42px">
    <div class="eyebrow">Our services</div>
    <h2>Complete Low Voltage<br>Infrastructure Solutions</h2>
    <p>Scalable commercial technology systems designed for performance, security, and<br>reliability.</p>
  </div>
  <article class="svc-card" style="left:61px"><div class="svc-photo" role="img" aria-label="Colour-coded wiring in a distribution panel"></div><span class="svc-arrow"><svg width="20" height="20" fill="none" stroke="#fff" stroke-width="2"><path d="M3 10h14M11 4l6 6-6 6"/></svg></span><h3>Residential Services</h3><p>Smart home cabling and Wi-Fi system for all your devices and security.</p><a class="btn btn-white">Contact Us</a></article>
  <article class="svc-card" style="left:427px"><div class="svc-photo" role="img" aria-label="Colour-coded wiring in a distribution panel"></div><span class="svc-arrow"><svg width="20" height="20" fill="none" stroke="#fff" stroke-width="2"><path d="M3 10h14M11 4l6 6-6 6"/></svg></span><h3>Residential Services</h3><p>Smart home cabling and Wi-Fi system for all your devices and security.</p><a class="btn btn-white">Contact Us</a></article>
  <article class="svc-card" style="left:792px"><div class="svc-photo" role="img" aria-label="Colour-coded wiring in a distribution panel"></div><span class="svc-arrow"><svg width="20" height="20" fill="none" stroke="#fff" stroke-width="2"><path d="M3 10h14M11 4l6 6-6 6"/></svg></span><h3>Residential Services</h3><p>Smart home cabling and Wi-Fi system for all your devices and security.</p><a class="btn btn-white">Contact Us</a></article>

  <div class="svc-icons">
    <div class="svc-icon" style="left:114px"><svg width="26" height="26" fill="none" stroke="#d42b1f" stroke-width="1.8"><path d="M23 3L3 11l8 4 4 8z"/></svg>Voice &amp; Data Cable<br>Installations</div>
    <div class="svc-icon" style="left:306px"><svg width="26" height="26" fill="none" stroke="#d42b1f" stroke-width="1.8"><path d="M6 3v8M10 3v8M4 11h8v4H4zM8 15v6M18 3v8M22 3v8M16 11h8v4h-8zM20 15v6"/></svg>Copper Cable CAT6<br>and CAT7</div>
    <div class="svc-icon" style="left:503px"><svg width="26" height="26" fill="none" stroke="#d42b1f" stroke-width="1.8"><circle cx="13" cy="13" r="10"/><path d="M13 7v6l4 3"/></svg>Fiber Cable Single &amp;<br>Multi Mode</div>
    <div class="svc-icon" style="left:697px"><svg width="26" height="26" fill="none" stroke="#d42b1f" stroke-width="1.8"><path d="M4 8v14h16M8 18l12-12 3 3-12 12H8z"/></svg>Conduit<br>Installations</div>
    <div class="svc-icon" style="left:892px"><svg width="26" height="26" fill="none" stroke="#d42b1f" stroke-width="1.8"><path d="M13 2v3M4 6l2 2M22 6l-2 2M2 14h3M21 14h3"/><path d="M8 16a5 5 0 1 1 10 0l-2 3h-6z"/><path d="M10 22h6"/></svg>IDF and MDF<br>Installations</div>
    <div class="svc-icon" style="left:1086px"><svg width="26" height="26" fill="none" stroke="#d42b1f" stroke-width="1.8"><rect x="5" y="4" width="16" height="20" rx="2"/><path d="M9 2h8v4H9zM9 12h8M9 17h8"/></svg>Link Tester<br>Certification</div>
  </div>
</section>

<section class="why">
  <div class="placeholder why-photo" role="img" aria-label="Engineer in safety glasses and high-visibility vest inspecting server equipment under red light"></div>
  <div class="abs eyebrow" style="left:61px;top:95px">Why choose us</div>
  <h2>Why Commercial Clients<br>Choose Wirenexa</h2>
  <p class="abs why-copy">We are a full service cabling company and will work with your IT staff to make sure everything up and running after installation and testing.</p>
  <div class="why-item" style="left:61px"><span class="dot"><svg width="22" height="22" fill="none" stroke="#fff" stroke-width="1.8"><path d="M11 2l8 3v6c0 5-4 8-8 9-4-1-8-4-8-9V5z"/></svg></span><h4>Safe &amp; Secure</h4><p>"Lorem ipsum dolor sit amet, consectetur adipiscing elit, sed do eiusmod</p></div>
  <div class="why-item" style="left:281px"><span class="dot"><svg width="22" height="22" fill="none" stroke="#fff" stroke-width="1.8"><circle cx="11" cy="11" r="8"/><path d="M11 6v5l3 2"/></svg></span><h4>24×7 Support</h4><p>"Lorem ipsum dolor sit amet, consectetur adipiscing elit, sed do eiusmod</p></div>
  <div class="why-item" style="left:501px"><span class="dot"><svg width="22" height="22" fill="none" stroke="#fff" stroke-width="1.8"><circle cx="11" cy="11" r="8"/><path d="M13.5 8c-1-1-5-1-5 1s5 1 5 3-4 2-5 1M11 5v2M11 15v2"/></svg></span><h4>Low Cost</h4><p>"Lorem ipsum dolor sit amet, consectetur adipiscing elit, sed do eiusmod</p></div>
</section>

<section class="partners">
  <div class="center-head" style="top:94px"><div class="eyebrow" style="font-size:11px">Trusted infrastructure partner for commercial businesses</div></div>
  <div class="partner" style="left:107px">Netwave</div>
  <div class="partner" style="left:295px;font-size:18px;top:176px">Skyline Labs</div>
  <div class="partner" style="left:506px">Arcfi</div>
  <div class="partner" style="left:786px">Vistaguard</div>
  <div class="partner" style="left:1060px">Lumeron</div>
</section>

<section class="quote">
  <div class="placeholder quote-photo" role="img" aria-label="Network technician in glasses working on a blue-lit patch panel"></div>
  <h2>Request a Quote Today</h2>
  <div class="abs display" style="left:533px;top:95px;color:#fff;font-size:22px">(888)-555-0142</div>
  <p class="abs" style="left:533px;top:136px;color:#fff;font-size:12px">Submit the form and we will contact you within 1 hour.</p>
  <div class="quote-field" style="top:172px;height:48px">Name Here</div>
  <div class="quote-field" style="top:250px;height:48px">Name Here</div>
  <div class="quote-field" style="top:327px;height:48px">Name Here</div>
  <div class="quote-field" style="top:403px;height:137px">Name Here</div>
  <a class="btn btn-red" style="left:533px;top:568px;width:622px;height:47px;font-size:13px;font-weight:500">Send Message</a>

  <div class="info-bar" style="top:481px"><svg width="16" height="16" viewBox="0 0 24 24" fill="none" stroke="#fff" stroke-width="2"><path d="M5 3h4l2 5-3 2a12 12 0 0 0 6 6l2-3 5 2v4a2 2 0 0 1-2 2A17 17 0 0 1 3 5a2 2 0 0 1 2-2z"/></svg><b>PHONE:</b><span style="margin-left:14px">LOCAL: 703-555-0190</span><span style="margin-left:10px">NATIONAL: (888) 555-0142</span></div>
  <div class="info-bar" style="top:551px"><svg width="16" height="16" fill="none" stroke="#fff" stroke-width="2"><rect x="1" y="3" width="14" height="10"/><path d="M1 3l7 6 7-6"/></svg><b>EMAIL :</b><span style="margin-left:14px">SALES@WIRENEXA.COM</span></div>
  <div class="info-bar" style="top:621px;font-size:10px"><svg width="16" height="16" fill="none" stroke="#fff" stroke-width="2"><path d="M15 1L1 7l6 2 2 6z"/></svg><b>LOCATION:</b><span style="margin-left:6px">4410 HARBOR POINT DR, SUITE 120 FAIRVIEW, VA 22031</span></div>
</section>

<section class="spacer"></section>

<footer class="footer">
  <div class="brand" style="left:63px;top:107px;font-size:38px"><span class="brand-mark" style="width:38px;height:38px"></span>Wirenexa</div>
  <div class="social" aria-label="Social media links"><span></span><span></span><span></span><span></span></div>
  <p class="abs" style="left:61px;top:180px;width:265px;font-size:11px;line-height:14px">Wirenexa is a local group of IT professionals, dedicated to fast, reliable and honest service. No job is too big or too small, get in touch today for solutions to all your IT infrastructure needs!</p>
  <a class="btn btn-red" style="left:61px;top:250px;width:162px;height:35px">Request Consultation</a>

  <h4 style="left:580px;top:95px">Company</h4>
  <ul class="foot-links" style="left:580px;top:125px"><li>Home</li><li>Services</li><li>About us</li><li>Contact us</li></ul>

  <h4 style="left:762px;top:95px">Contact us</h4>
  <div class="foot-contact" style="left:762px;top:140px"><b>☏ PHONE:</b><br>(888)-555-0142</div>
  <div class="foot-contact" style="left:762px;top:187px"><b>✉ EMAIL</b><br>sales@wirenexa.com</div>
  <div class="foot-contact" style="left:762px;top:234px"><b>➤ LOCATION</b><br>4410 Harbor Point Dr,<br>Suite 120<br><br>Fairview, VA 22031</div>

  <div class="abs" style="left:950px;top:135px;width:150px;height:150px;border-radius:50%;background:linear-gradient(135deg,#f4b400,#d42b1f 50%,#2a7fc1)" role="img" aria-label="Anniversary badge"></div>

  <div class="legal"><span>© Brightpath Inc. All Rights Reserved.</span><nav><a href="#">Cookies Settings</a><a href="#">Terms &amp; Condition</a><a href="#">Privacy policy</a></nav></div>
</footer>

</body>
</html>
```